Business Card for TKR, logo files already created

Please, can you assist with creating a Business card the TKR graphics which are already listed on www.tarnkeyrelay.example
The business card should be modern and upmarket, textured designs are welcome. Please feel free to express yourself and be very bold with your design.

Target Market(s)

Cyber Security

Industry/Entity Type

Information Technology

Contact Information for Business Card

Company Name
Name
Title
Mobile
Fax or Tel
email
url

Font styles to use
Serif
Sans Serif

Colors
3277b5
85acd3
ffffff

```html
<!DOCTYPE html>
<html lang="en">
<head>
<meta charset="utf-8">
<title>TKR Business Card</title>
<link href="https://fonts.googleapis.com/css2?family=Montserrat:wght@400;600;700;800&family=Open+Sans:wght@400&display=swap" rel="stylesheet">
<style>
  :root {
    --bg: #e9ebef;
    --navy: #121848;
    --navy-deep: #0e1440;
    --teal: #2a6f8e;
    --ice: #dfe9f5;
    --white: #ffffff;
    --paper: #fbfbfb;
    --ink: #1a2058;
    --grey: #6b6f7a;
  }
  * { box-sizing: border-box; margin: 0; padding: 0; }
  html, body { width: 1200px; height: 850px; overflow: hidden; }
  body {
    background: var(--bg);
    position: relative;
    font-family: "Open Sans", Arial, sans-serif;
  }
  .card {
    position: absolute;
    width: 520px;
    height: 298px;
    border-radius: 3px;
    overflow: hidden;
    box-shadow: 0 8px 22px rgba(20, 24, 60, 0.22);
  }
  .card-front {
    left: 50px;
    top: 190px;
    background: radial-gradient(circle at 0% 100%, var(--teal) 0%, rgba(42,111,142,0) 48%), linear-gradient(135deg, var(--navy) 0%, var(--navy-deep) 100%);
  }
  .front-arcs { position: absolute; right: 0; bottom: 0; }
  .front-logo {
    position: absolute;
    left: 0; right: 0; top: 62px;
    text-align: center;
    color: var(--ice);
  }
  .front-logo .mark {
    font-family: "Montserrat", Arial, sans-serif;
    font-weight: 800;
    font-size: 86px;
    line-height: 1;
    letter-spacing: 2px;
  }
  .front-logo .company {
    display: inline-block;
    margin-top: 8px;
    padding: 5px 14px;
    border-top: 1.5px solid var(--ice);
    border-bottom: 1.5px solid var(--ice);
    font-family: "Montserrat", Arial, sans-serif;
    font-weight: 800;
    font-size: 19px;
    letter-spacing: 2px;
  }
  .front-logo .tagline {
    margin-top: 8px;
    font-family: "Montserrat", Arial, sans-serif;
    font-weight: 400;
    font-size: 12px;
    letter-spacing: 2.4px;
    color: var(--white);
  }

  .card-back {
    left: 630px;
    top: 370px;
    background: var(--paper);
  }
  .back-panel {
    position: absolute;
    left: 0; top: 0; bottom: 0;
    width: 318px;
    background: radial-gradient(circle at 0% 100%, var(--teal) 0%, rgba(42,111,142,0) 55%), linear-gradient(135deg, var(--navy) 0%, var(--navy-deep) 100%);
  }
  .back-logo {
    position: absolute;
    left: 30px; top: 30px;
    display: flex;
    align-items: center;
    gap: 8px;
    color: var(--ice);
    font-family: "Montserrat", Arial, sans-serif;
    font-weight: 800;
  }
  .back-logo .mark { font-size: 30px; letter-spacing: 1px; }
  .back-logo .divider { width: 1px; height: 30px; background: var(--ice); }
  .back-logo .company { font-size: 9px; line-height: 1.15; letter-spacing: 0.8px; }
  .contact-list {
    position: absolute;
    left: 30px; top: 162px;
    list-style: none;
    color: var(--white);
    font-size: 11.5px;
  }
  .contact-list li {
    display: flex;
    align-items: center;
    gap: 8px;
    height: 22px;
  }
  .contact-list svg { width: 11px; height: 11px; flex: none; }
  .person {
    position: absolute;
    right: 28px; top: 150px;
    text-align: right;
    font-family: "Montserrat", Arial, sans-serif;
  }
  .person .name { font-size: 17px; color: var(--ink); letter-spacing: 0.5px; }
  .person .name b { font-weight: 700; }
  .person .name span { font-weight: 400; }
  .person .title { font-size: 9px; color: var(--grey); letter-spacing: 1px; margin-top: 2px; }
  .side-tab {
    position: absolute;
    right: 0; top: 168px;
    width: 12px; height: 40px;
    background: var(--navy);
  }
</style>
</head>
<body>
  <section class="card card-front" aria-label="Card front">
    <svg class="front-arcs" width="260" height="180" viewBox="0 0 260 180" aria-hidden="true">
      <circle cx="210" cy="190" r="130" fill="none" stroke="#2f4a86" stroke-opacity="0.45" stroke-width="1"/>
      <circle cx="210" cy="190" r="105" fill="none" stroke="#2a6f8e" stroke-opacity="0.5" stroke-width="1"/>
    </svg>
    <div class="front-logo">
      <div class="mark">TKR</div>
      <div class="company">TARNKEY RELAY SOLUTIONS</div>
      <div class="tagline">INTELLIGENCE - DRIVEN SOLUTIONS</div>
    </div>
  </section>

  <section class="card card-back" aria-label="Card back">
    <div class="back-panel">
      <div class="back-logo">
        <span class="mark">TKR</span>
        <span class="divider"></span>
        <span class="company">TARNKEY RELAY<br>SOLUTIONS</span>
      </div>
      <ul class="contact-list">
        <li>
          <svg viewBox="0 0 12 12"><rect x="3" y="0.5" width="6" height="11" rx="1" fill="none" stroke="#fff"/><circle cx="6" cy="9.6" r="0.7" fill="#fff"/></svg>
          123-456-7890
        </li>
        <li>
          <svg viewBox="0 0 12 12"><path d="M1 4 Q6 1 11 4 L10 5.5 L8 5 L8 4 Q6 3.3 4 4 L4 5 L2 5.5 Z" fill="#fff"/><rect x="2.5" y="6" width="7" height="5" rx="1" fill="#fff"/></svg>
          123-456-7890
        </li>
        <li>
          <svg viewBox="0 0 12 12"><rect x="0.5" y="2" width="11" height="8" fill="#fff"/><path d="M0.5 2 L6 7 L11.5 2" fill="none" stroke="#121848"/></svg>
          contact@tarnkeyrelay.example
        </li>
        <li>
          <svg viewBox="0 0 12 12"><circle cx="6" cy="6" r="5.2" fill="none" stroke="#fff"/><ellipse cx="6" cy="6" rx="2.3" ry="5.2" fill="none" stroke="#fff"/><path d="M0.8 6 H11.2" stroke="#fff"/></svg>
          www.tarnkeyrelay.example
        </li>
      </ul>
    </div>
    <div class="person">
      <div class="name"><b>OWEN</b> <span>HALE</span></div>
      <div class="title">FOUNDER AND CEO</div>
    </div>
    <div class="side-tab"></div>
  </section>
</body>
</html>
```